Korvane Systems Website

Website design for our company: Korvane Systems.
The website should look fresh and IT focused. Please have a look at http://www.korvanesystems.example.au/ for our current design. We want something fresh and new, professional looking, in WordPress so we can easily make changes.

Industry/Entity Type

It Company

```html
<!DOCTYPE html>
<html lang="en">
<head>
<meta charset="utf-8">
<title>Korvane Systems</title>
<link href="https://fonts.googleapis.com/css2?family=Open+Sans:wght@400;600;700&display=swap" rel="stylesheet">
<style>
:root{
  --green-top:#1a9a4e;
  --green-deep:#0e6b33;
  --green-bright:#13b14f;
  --footer-top:#2a7d4c;
  --footer-bottom:#175c35;
  --footer-bar:#154d2d;
  --link-blue:#2e7fb5;
  --read-green:#1f6d3c;
  --text:#555;
  --text-light:#777;
  --nav:#0a0a0a;
  --white:#fff;
}
*{margin:0;padding:0;box-sizing:border-box}
html,body{width:914px;height:1200px;overflow:hidden;background:var(--white)}
body{position:relative;font-family:"Open Sans",Arial,sans-serif;color:var(--text)}
.abs{position:absolute}
.site-header{left:0;top:0;width:914px;height:134px;background:linear-gradient(180deg,var(--green-top),var(--green-deep))}
.brand{left:75px;top:18px;width:131px;height:65px;background:var(--green-bright);border:2px solid #e9f6ee;border-radius:4px;display:flex;align-items:center;justify-content:center;gap:6px}
.brand-mark{width:12px;height:12px;background:var(--white)}
.brand-name{color:var(--white);font-weight:600;font-size:14px;line-height:1.1;text-align:left}
.phone{right:79px;top:40px;text-align:right;color:var(--white)}
.phone-label{font-size:14px;font-weight:400;opacity:.95}
.phone-number{font-size:19px;font-weight:400;margin-top:1px;letter-spacing:.2px}
.main-nav{left:74px;top:95px;width:766px;height:39px;background:var(--nav);display:flex;border:1px solid #333;border-bottom:none}
.main-nav a{color:var(--white);font-weight:700;font-size:12px;text-decoration:none;display:flex;align-items:center;justify-content:center;border-right:1px solid #3a3a3a}
.main-nav a:last-child{border-right:none}
.hero{left:74px;top:134px;width:766px;height:307px;background:linear-gradient(180deg,#e9e9e9 0%,#cfcfcf 45%,#f2f2f2 100%);border:1px solid #ddd}
.hero-caption{left:74px;top:232px;width:362px;height:126px;background:rgba(60,60,60,.82);padding:15px 10px 0 24px;overflow:hidden}
.hero-title{color:var(--green-bright);font-size:25px;font-weight:400;line-height:30px;white-space:nowrap}
.hero-sub{color:var(--white);font-size:20px;line-height:26px}
.hero-text{color:#ddd;font-size:9px;line-height:15px;margin-top:4px;width:270px}
.slider-dots{left:433px;top:419px;display:flex;gap:3px}
.slider-dots span{width:11px;height:11px;border-radius:50%;background:#333}
.service{top:458px}
.service-photo{width:184px;height:84px}
.service h3{font-size:15px;font-weight:400;color:var(--link-blue);margin-top:9px}
.service p{font-size:10px;line-height:16px;color:var(--text-light);margin-top:1px}
.service a{display:block;font-size:11px;font-weight:600;color:var(--read-green);text-decoration:none;margin-top:1px}
.welcome{left:74px;top:690px;width:520px}
.welcome h1{font-size:23px;font-weight:400;color:var(--green-bright)}
.welcome .lead{font-size:11.5px;line-height:16.5px;margin-top:9px;color:#555}
.welcome p{font-size:9.5px;line-height:16.5px;margin-top:7px;color:#555}
.contact-form{left:648px;top:678px;width:192px;height:204px;border:1px solid #ccc;background:var(--white)}
.contact-form h2{font-size:16px;font-weight:400;color:#333;height:38px;padding:9px 19px;background:linear-gradient(180deg,#fff,#f3f3f3);border-bottom:1px solid #ddd}
.field{display:block;margin:12px 0 0 18px;width:160px;height:22px;border:1px solid #ccc;border-radius:2px;font-size:9px;color:#555;padding:5px 9px}
.field+.field{margin-top:7px}
.submit{margin:8px 0 0 18px;width:74px;height:24px;background:#0f4a25;color:var(--white);font-size:11px;font-weight:600;display:flex;align-items:center;justify-content:center;border-radius:2px}
.site-footer{left:0;top:933px;width:914px;height:213px;background:linear-gradient(180deg,var(--footer-top),var(--footer-bottom))}
.footer-col{top:965px;color:var(--white)}
.footer-col h4{font-size:13.5px;font-weight:600;margin-bottom:8px}
.footer-col li{list-style:none;font-size:10px;line-height:18.7px;padding-left:2px}
.footer-bar{left:0;top:1146px;width:914px;height:54px;background:var(--footer-bar)}
.copyright{left:72px;top:1163px;font-size:9.5px;color:var(--white)}
.social{left:744px;top:1163px;display:flex;gap:6px}
.social span{width:15px;height:15px;border-radius:2px}
</style>
</head>
<body>
<header class="site-header abs"></header>
<div class="brand abs"><span class="brand-mark"></span><span class="brand-name">Korvane<br>Systems</span></div>
<div class="phone abs"><div class="phone-label">Phone Support</div><div class="phone-number">868.5550.0142</div></div>
<nav class="main-nav abs">
  <a href="#" style="width:84px">HOME</a>
  <a href="#" style="width:110px">ABOUT US</a>
  <a href="#" style="width:95px">CLIENTS</a>
  <a href="#" style="width:104px">SERVICES</a>
  <a href="#" style="width:109px">SUPPORTS</a>
  <a href="#" style="width:129px">TESTIMONIALS</a>
  <a href="#" style="width:135px">CONTACT US</a>
</nav>

<div class="hero abs" role="img" aria-label="Photo of a bright data centre with rows of server racks"></div>
<div class="hero-caption abs">
  <div class="hero-title">Computer and IT Services</div>
  <div class="hero-sub">Aliquam erat purus cursus</div>
  <div class="hero-text">Etiam eu urna Sed porta Suspendisse quam leo molestie sed luctus quis feugiat in pede Fusce tellus Sed metus</div>
</div>
<div class="slider-dots abs"><span></span><span></span><span></span><span></span></div>

<div class="service abs" style="left:74px">
  <div class="service-photo" role="img" aria-label="Photo of a support technician wearing a headset" style="background:linear-gradient(135deg,#b07a3a,#6b4a25)"></div>
  <h3>On-site Service</h3>
  <p>Pellentesque faucibus Ut accumsan<br>ultricies elit Maecenas at justo</p>
  <a href="#">Read More</a>
</div>
<div class="service abs" style="left:266px">
  <div class="service-photo" role="img" aria-label="Photo of a help desk operator at a computer" style="background:linear-gradient(135deg,#e8e8e8,#9aa4b0)"></div>
  <h3>Remote Desktop Support</h3>
  <p>Pellentesque faucibus Ut accumsan<br>ultricies elit Maecenas at justo</p>
  <a href="#">Read More</a>
</div>
<div class="service abs" style="left:462px;width:180px">
  <div class="service-photo" role="img" aria-label="Photo of technicians working in a server room" style="width:180px;background:linear-gradient(135deg,#7f8f8a,#3f6f5f)"></div>
  <h3>Medical IT Service</h3>
  <p>Pellentesque faucibus Ut accumsan<br>ultricies elit Maecenas at justo</p>
  <a href="#">Read More</a>
</div>
<div class="service abs" style="left:651px">
  <div class="service-photo" role="img" aria-label="Photo of staff helping at a computer workstation" style="background:linear-gradient(135deg,#d8dde3,#8a9aac)"></div>
  <h3>Pharmacy IT Service</h3>
  <p>Pellentesque faucibus Ut accumsan<br>ultricies elit Maecenas at justo</p>
  <a href="#">Read More</a>
</div>

<section class="welcome abs">
  <h1>Welcome to Korvane Systems Mainpage</h1>
  <p class="lead">Korvane Systems is an Adelaide based company with a single objective - to excel in the support and service of all computer and IT needs.</p>
  <p>We provide a high level of consulting services using the most experienced engineers at a reasonable and fair price. We believe in using a Business Value approach to every aspect of computer consulting to provide our clients with the most cost effective solutions.</p>
  <p>We strongly believe that we are in business with our clients. Each thing we do must be measured against our clients' business objectives. At the end of the day our client's success is our success.</p>
</section>

<form class="contact-form abs">
  <h2>Fill Contact Form</h2>
  <span class="field">Full Name</span>
  <span class="field">Email address</span>
  <span class="field">Phone no.</span>
  <span class="field">Message</span>
  <span class="submit">SUBMIT</span>
</form>

<footer class="site-footer abs"></footer>
<div class="footer-col abs" style="left:80px"><h4>COMPANY</h4><ul><li>About Us</li><li>Services</li><li>Solutions</li><li>Case Studies</li><li>Awards</li></ul></div>
<div class="footer-col abs" style="left:224px"><h4>FEATURES</h4><ul><li>Sed porta</li><li>Suspendisse quam</li><li>Leo molestie</li><li>Sed luctus quis</li><li>Tempor cursus</li></ul></div>
<div class="footer-col abs" style="left:381px"><h4>SERVICES</h4><ul><li>Phasellus felis dolor</li><li>Scelerisque tempus</li><li>Eget lobortis</li><li>Libero Aliquam</li></ul></div>
<div class="footer-col abs" style="left:539px"><h4>SUPPORT</h4><ul><li>Sed porta</li><li>Suspendisse quam</li><li>Leo molestie</li><li>Sed luctus quis</li></ul></div>
<div class="footer-col abs" style="left:681px"><h4>CONTACT</h4><ul><li>48 Calloway Rd, Suite 12</li><li>Brenton, Ohio 40217 US</li><li>Tel: +44 (0)1632 960418</li><li>hello@korvane.example</li></ul></div>

<div class="footer-bar abs"></div>
<div class="copyright abs">© 2014 Company Name.&nbsp; All right reserved.&nbsp; Term of Use</div>
<div class="social abs" aria-label="Social links">
  <span style="background:#3b5a98"></span>
  <span style="background:#3aa6dc"></span>
  <span style="background:#1f6fa3"></span>
  <span style="background:#e8861f"></span>
</div>
</body>
</html>
```